5X8" post card hand outs listing our contracting services

Hello We are a Environmental contracting firm and i would like to have flyers made up around 5X8" of so, front and back. I have attached what we have now for your review. Its not great but it does work however, we need a remodel and are open to changes and revisions. Our services include excavating, grading, environmental remediation, liquid and bulk transportation services, AST / UST tank removals and waste management and waste disposal Thank you!

Target Market(s)

Environmental Consulting firms, other business to business related contractors, state and govt.

Industry/Entity Type

Environmental contracting, Environmental remediation, fuel station tank removals, excavating, trucking and waste management

Font styles to use
Serif

Colors
0054AA
0677BA
7BADD7
CADEEF
E8F1F8

Requirements
Must have
• The info that is listed on the provided hand out.

```html
<!DOCTYPE html>
<html lang="en">
<head>
<meta charset="utf-8">
<title>Kestrel Environmental Group – Flyer</title>
<link href="https://fonts.googleapis.com/css2?family=Montserrat:wght@400;500;600;700;800&family=Hind:wght@400;500;600&display=swap" rel="stylesheet">
<style>
  :root{
    --navy:#0054AA;
    --royal:#1A4FA0;
    --ocean:#0677BA;
    --sky:#7BADD7;
    --mist:#CADEEF;
    --frost:#E8F1F8;
    --ink:#3a4a5c;
    --stage:#bdbdbf;
    --photo-dark:#1b2a4a;
    --photo-mid:#34507a;
  }
  *{margin:0;padding:0;box-sizing:border-box}
  html,body{width:1200px;height:957px;overflow:hidden;background:var(--stage)}
  body{position:relative;font-family:'Hind',sans-serif}

  .sheet{position:absolute;top:129px;width:462px;height:739px;overflow:hidden;background:#fff}
  .sheet--front{left:117px}
  .sheet--back{left:629px;background:var(--frost)}
  .sheet-bg{position:absolute;inset:0;width:100%;height:100%}

  /* wordmark */
  .wordmark{position:absolute;color:#fff;font-family:'Montserrat',sans-serif;text-align:center}
  .wordmark .name{font-weight:800;letter-spacing:.12em;display:block;line-height:1}
  .wordmark .sub{font-weight:700;display:block;white-space:nowrap}
  .sheet--front .wordmark{left:306px;top:30px;width:144px}
  .sheet--front .wordmark .name{font-size:22px}
  .sheet--front .wordmark .sub{font-size:7.6px;margin-top:8px}
  .sheet--back .wordmark{left:338px;top:650px;width:90px}
  .sheet--back .wordmark .name{font-size:14px}
  .sheet--back .wordmark .sub{font-size:4.6px;margin-top:5px}

  /* hero circle text */
  .hero-title{position:absolute;left:6px;top:258px;font-family:'Montserrat',sans-serif;color:var(--ink);font-size:17px;line-height:25px;font-weight:500}
  .hero-title strong{font-weight:700}
  .hero-rule{position:absolute;left:7px;top:335px;width:86px;border-top:1px dashed var(--ink)}
  .hero-tag{position:absolute;left:7px;top:342px;font-family:'Montserrat',sans-serif;font-size:5.4px;line-height:10px;color:var(--ink);font-weight:500}

  /* service pills */
  .pill{position:absolute;height:58px}
  .pill svg.shape{position:absolute;left:0;top:0}
  .pill .icon{position:absolute;left:7px;top:6px;width:46px;height:46px;border-radius:50%;background:var(--mist);border:2px solid #fff}
  .pill .label{position:absolute;left:70px;top:0;height:58px;display:flex;align-items:center;color:#fff;font-family:'Montserrat',sans-serif;font-weight:700;font-size:10.6px;line-height:13px}
  .pill .badge{position:absolute;top:-13px;width:22px;height:22px;border-radius:50%;background:#fff;border:1.5px solid var(--sky);color:var(--sky);font-family:'Montserrat',sans-serif;font-size:8px;font-weight:600;display:flex;align-items:center;justify-content:center}

  .pledge{position:absolute;left:60px;top:600px;width:400px;text-align:center;color:var(--navy);font-size:11px;line-height:15.4px;font-weight:500}
  .contact-front{position:absolute;right:23px;top:676px;text-align:right;color:#fff;font-family:'Montserrat',sans-serif}
  .contact-front .lead{font-size:12.5px;font-weight:400;display:flex;align-items:center;justify-content:flex-end;gap:4px}
  .contact-front .phone{font-size:15.5px;font-weight:500;margin-top:6px}

  .photo{position:absolute}

  /* back: sections */
  .section-head{position:absolute;left:37px;width:280px;height:56px}
  .section-head .bar{position:absolute;left:40px;top:8px;right:0;height:42px;background:var(--ocean);border-radius:0 6px 6px 0}
  .section-head .num{position:absolute;left:0;top:0;width:56px;height:56px;background:var(--navy);border-radius:10px;color:#fff;font-family:'Montserrat',sans-serif;font-weight:700;font-size:20px;display:flex;align-items:center;justify-content:center}
  .section-head .title{position:absolute;left:68px;top:8px;height:42px;display:flex;align-items:center;color:#fff;font-family:'Montserrat',sans-serif;font-weight:600;font-size:15.5px}
  .service-list{position:absolute;left:37px;list-style:none;color:#1d2a3a;font-size:13.4px;line-height:13px}
  .service-list li{position:relative;padding-left:19px}
  .service-list li::before{content:"";position:absolute;left:2px;top:4px;width:4px;height:4px;border-radius:50%;background:#1d2a3a}

  .contact-back{position:absolute;left:120px;top:630px;width:190px;text-align:center;color:#fff}
  .contact-icons{display:flex;justify-content:center;gap:28px;margin-left:4px}
  .contact-icons span{width:28px;height:28px;background:var(--royal);border-radius:3px;display:flex;align-items:center;justify-content:center}
  .contact-back .mail{font-size:13.5px;margin-top:8px;letter-spacing:.02em}
  .contact-back .phone{font-family:'Montserrat',sans-serif;font-weight:600;font-size:11.5px;margin-top:3px}
</style>
</head>
<body>

<!-- FRONT -->
<section class="sheet sheet--front">
  <svg class="sheet-bg" viewBox="0 0 462 739" aria-hidden="true">
    <polygon points="40,0 462,0 462,74 233,34" fill="var(--royal)"/>
    <polygon points="233,34 462,74 462,158" fill="#6592cc"/>
    <!-- arc + connectors -->
    <circle cx="9" cy="310" r="163" fill="none" stroke="var(--sky)" stroke-width="1.6"/>
    <line x1="55" y1="161" x2="72" y2="128" stroke="var(--sky)" stroke-width="1.6"/>
    <line x1="50" y1="461" x2="70" y2="512" stroke="var(--sky)" stroke-width="1.6"/>
    <line x1="110" y1="193" x2="150" y2="182" stroke="var(--sky)" stroke-width="1.6"/>
    <line x1="167" y1="271" x2="200" y2="271" stroke="var(--sky)" stroke-width="1.6"/>
    <line x1="167" y1="359" x2="200" y2="359" stroke="var(--sky)" stroke-width="1.6"/>
    <line x1="128" y1="420" x2="155" y2="436" stroke="var(--sky)" stroke-width="1.6"/>
    <g fill="var(--sky)">
      <circle cx="55" cy="161" r="4"/><circle cx="110" cy="193" r="4"/>
      <circle cx="167" cy="271" r="4"/><circle cx="167" cy="359" r="4"/>
      <circle cx="128" cy="420" r="4"/><circle cx="50" cy="461" r="4"/>
    </g>
    <!-- hero ring -->
    <circle cx="9" cy="310" r="142" fill="var(--navy)"/>
    <circle cx="9" cy="310" r="115" fill="var(--frost)"/>
    <!-- bottom bands -->
    <polygon points="202,713 462,623 462,739 236,739" fill="var(--royal)"/>
  </svg>
  <svg class="photo" style="left:0;top:566px" width="236" height="173" viewBox="0 0 236 173" role="img" aria-label="Photo of a crew member working beside a vacuum truck">
    <defs><linearGradient id="photoFront" x1="0" y1="0" x2="1" y2="1"><stop offset="0" stop-color="var(--photo-mid)"/><stop offset="1" stop-color="var(--photo-dark)"/></linearGradient></defs>
    <polygon points="0,0 236,173 0,173" fill="url(#photoFront)"/>
  </svg>

  <div class="wordmark"><span class="name">KESTREL</span><span class="sub">ENVIRONMENTAL GROUP LLC</span></div>

  <h1 class="hero-title">VACUUM<br>TRUCK<br><strong>SERVICES</strong></h1>
  <div class="hero-rule"></div>
  <p class="hero-tag">A FULL SERVICE<br>ENVIRONMENTAL COMPANY</p>

  <div class="pill" style="left:52px;top:71px;width:189px">
    <svg class="shape" width="189" height="58"><path d="M29 0H161L189 29L161 58H29A29 29 0 0 1 29 0Z" fill="var(--royal)"/></svg>
    <div class="icon" role="img" aria-label="Recycling icon"></div>
    <div class="label">REMEDIATION</div>
    <div class="badge" style="left:137px">01</div>
  </div>
  <div class="pill" style="left:144px;top:153px;width:188px">
    <svg class="shape" width="188" height="58"><path d="M29 0H160L188 29L160 58H29A29 29 0 0 1 29 0Z" fill="var(--royal)"/></svg>
    <div class="icon" role="img" aria-label="Storage tank icon"></div>
    <div class="label">AST &amp; UST<br>TANK REMOVALS</div>
    <div class="badge" style="left:134px">02</div>
  </div>
  <div class="pill" style="left:197px;top:242px;width:190px">
    <svg class="shape" width="190" height="58"><path d="M29 0H162L190 29L162 58H29A29 29 0 0 1 29 0Z" fill="var(--royal)"/></svg>
    <div class="icon" role="img" aria-label="Delivery truck icon"></div>
    <div class="label">BULK<br>TRANSPORTATION</div>
    <div class="badge" style="left:134px">03</div>
  </div>
  <div class="pill" style="left:197px;top:330px;width:190px">
    <svg class="shape" width="190" height="58"><path d="M29 0H162L190 29L162 58H29A29 29 0 0 1 29 0Z" fill="var(--royal)"/></svg>
    <div class="icon" role="img" aria-label="Hazard sampling icon"></div>
    <div class="label">WASTE SAMPLING<br>AND PROFILING</div>
    <div class="badge" style="left:133px">04</div>
  </div>
  <div class="pill" style="left:150px;top:423px;width:189px">
    <svg class="shape" width="189" height="58"><path d="M29 0H161L189 29L161 58H29A29 29 0 0 1 29 0Z" fill="var(--royal)"/></svg>
    <div class="icon" role="img" aria-label="Tank cleaning worker icon"></div>
    <div class="label">TANK CLEANING</div>
    <div class="badge" style="left:138px">05</div>
  </div>
  <div class="pill" style="left:55px;top:512px;width:189px">
    <svg class="shape" width="189" height="58"><path d="M29 0H161L189 29L161 58H29A29 29 0 0 1 29 0Z" fill="var(--royal)"/></svg>
    <div class="icon" role="img" aria-label="Waste in hands icon"></div>
    <div class="label">WASTE<br>MANAGEMENT</div>
    <div class="badge" style="left:132px">06</div>
  </div>

  <p class="pledge">Safety and compliance is our key focus at Kestrel Environmental Group.<br>All of our employees are OSHA, Hazwoper and DOT certified.<br>We operate with integrity, pride and professionalism<br>each and every day</p>

  <div class="contact-front">
    <div class="lead">
      <svg width="12" height="12" viewBox="0 0 12 12" aria-hidden="true"><circle cx="6" cy="6" r="5.3" fill="none" stroke="#fff" stroke-width="1"/><path d="M4 3.2l1 1.3-.6.7a4 4 0 0 0 1.9 1.9l.7-.6 1.3 1-.6 1.1C5.6 8.5 3.5 6.4 3.3 4z" fill="#fff"/></svg>
      Contact us:
    </div>
    <div class="phone">+ (555) 014 2290</div>
  </div>
</section>

<!-- BACK -->
<section class="sheet sheet--back">
  <svg class="sheet-bg" viewBox="0 0 462 739" aria-hidden="true">
    <polygon points="66,0 462,0 462,76" fill="var(--royal)"/>
    <polygon points="260,36 462,76 462,155" fill="var(--ocean)"/>
    <polygon points="392,105 462,155 462,575 456,575" fill="#6aa2d4"/>
  </svg>
  <svg class="photo" style="left:0;top:575px" width="462" height="164" viewBox="0 0 462 164" role="img" aria-label="Photo of a white vacuum truck parked outdoors">
    <defs><linearGradient id="photoBack" x1="0" y1="0" x2="1" y2="1"><stop offset="0" stop-color="var(--photo-dark)"/><stop offset=".6" stop-color="var(--photo-mid)"/><stop offset="1" stop-color="#6f8fb8"/></linearGradient></defs>
    <polygon points="0,115 94,99 456,0 462,0 462,164 0,164" fill="url(#photoBack)"/>
  </svg>
  <svg class="sheet-bg" viewBox="0 0 462 739" aria-hidden="true" style="pointer-events:none">
    <polygon points="0,597 94,674 0,700" fill="var(--royal)"/>
  </svg>

  <div class="section-head" style="top:60px">
    <div class="bar"></div><div class="num">01</div><div class="title">Vacuum truck services</div>
  </div>
  <ul class="service-list" style="top:130px">
    <li style="margin-bottom:7px">Waste water transportation</li>
    <li style="margin-bottom:6px">Oil water separators, grit chambers, tanks<br>and clarifier cleaning</li>
    <li style="margin-bottom:6px">Straight truck and tractor trailer service</li>
    <li style="margin-bottom:6px">AFVR services</li>
    <li>Tank pumping</li>
  </ul>

  <div class="section-head" style="top:247px">
    <div class="bar"></div><div class="num">02</div><div class="title">Waste management</div>
  </div>
  <ul class="service-list" style="top:312px">
    <li style="margin-bottom:6px">Solid waste transportation and disposal</li>
    <li style="margin-bottom:6px">Drum and tote management</li>
    <li style="margin-bottom:6px">Waste sampling, profiling and manifesting</li>
    <li style="margin-bottom:6px">Non hazardous, hazardous and e-waste recycling</li>
    <li>Fuel recycling</li>
  </ul>

  <div class="section-head" style="top:418px">
    <div class="bar"></div><div class="num">03</div><div class="title">Remediation</div>
  </div>
  <ul class="service-list" style="top:489px">
    <li style="margin-bottom:7px">Soil and ground water contamination excavating<br>and disposal</li>
    <li style="margin-bottom:8px">AST &amp; UST removal</li>
    <li style="margin-bottom:8px">Facility demolition, excavation and site work</li>
    <li style="margin-bottom:8px">Lagoon cleaning and closure</li>
    <li>Landfill remediation and RAP implementation</li>
  </ul>

  <div class="contact-back">
    <div class="contact-icons">
      <span><svg width="16" height="14" viewBox="0 0 16 14" aria-hidden="true"><rect x="2" y="1" width="12" height="9" rx="1" fill="none" stroke="#fff" stroke-width="1.5"/><rect x="0" y="11" width="16" height="2" fill="#fff"/></svg></span>
      <span><svg width="10" height="16" viewBox="0 0 10 16" aria-hidden="true"><rect x="1" y="1" width="8" height="14" rx="1.5" fill="none" stroke="#fff" stroke-width="1.5"/><circle cx="5" cy="12.5" r=".9" fill="#fff"/></svg></span>
      <span><svg width="16" height="12" viewBox="0 0 16 12" aria-hidden="true"><rect x="0" y="0" width="16" height="12" rx="1" fill="#fff"/><path d="M1 1l7 6 7-6" fill="none" stroke="var(--royal)" stroke-width="1.4"/></svg></span>
    </div>
    <div class="mail">office@kestrelenv.com</div>
    <div class="phone">(555) 014 2290</div>
  </div>

  <div class="wordmark"><span class="name">KESTREL</span><span class="sub">ENVIRONMENTAL GROUP, LLC</span></div>
</section>

</body>
</html>
```